依頼詳細
この企画実施のため、名古屋市内の全小学校に同様のデザインでポスターとチラシ配布を行うもの。
記載項目
施設名、電話番号、住所、ホームページへのリンク用QRコードを記載ください。
サイズ
A4
ページ数
片面
希望イメージ
シンプル 複雑
単色 カラフル
暗い 明るい
日常 高級
遊び心 厳粛
未来的 伝統的
女性的 男性的
希望する色
黄・オレンジ系
納品ファイル
• 高解像度JPG (.jpg)
補足説明
PDFデータもあわせて頂きます。

まずは初校提案をお願いします。
正式に依頼するとなったあと、数回文言修正のお願いをすることになります。

イベントの目的・主旨としては
ボルダリングジムPR促進、加えて、ボルダリング人口増を目的としています。
※特に、ボルダリングが「頭と身体を使う全身運動。体幹・想像力醸成に寄与」である旨PRしたく
また、“小学生”“初心者”に限定して実施することにより、その後親子での定期的な来場につなげる。

全体のバランスが良かったです

みなさま、今回応募頂きありがとうございます。
数多く応募頂き、それぞれ個性的であり、今回もかなり悩んで選択いたしました。
今後もよろしくお願いいたします。

```html
<!DOCTYPE html>
<html lang="ja">
<head>
<meta charset="utf-8">
<title>小学生限定 ボルダリング体験会 2022 Summer</title>
<link rel="stylesheet" href="https://fonts.googleapis.com/css2?family=M+PLUS+Rounded+1c:wght@500;700;800;900&family=Noto+Sans+JP:wght@400;700;900&display=swap">
<style>
:root{
  --yellow:#ffd93a;
  --yellow-soft:#fff3b0;
  --orange:#f39800;
  --orange-deep:#e8610f;
  --red:#e60033;
  --brown:#7a3b12;
  --navy:#1d2f6f;
  --ink:#333;
  --white:#fff;
  --photo-a:#d8e4ec;
  --photo-b:#b9c9d6;
}
*{box-sizing:border-box;margin:0;padding:0}
html,body{width:846px;height:1200px;overflow:hidden}
body{font-family:"Noto Sans JP",sans-serif;color:var(--ink);background:var(--white)}
.flyer{position:relative;width:846px;height:1200px;background:var(--yellow);overflow:hidden}
.lead{position:absolute;left:0;top:0;width:846px;height:72px;background:var(--white);
  display:flex;align-items:center;justify-content:center;text-align:center;
  font:700 22px/1.35 "M PLUS Rounded 1c",sans-serif;color:var(--orange-deep)}
.waves{position:absolute;right:0;top:72px}
.tagline{position:absolute;left:0;width:100%;top:84px;display:flex;justify-content:center;align-items:center;gap:14px}
.tag-beginner{background:var(--red);color:var(--white);font:900 30px "M PLUS Rounded 1c",sans-serif;padding:2px 22px;border-radius:10px}
.tag-kids{font:900 38px "M PLUS Rounded 1c",sans-serif;color:var(--red)}
.title{position:absolute;left:0;width:100%;top:130px;text-align:center;
  font:900 80px/1 "M PLUS Rounded 1c",sans-serif;color:var(--orange);
  -webkit-text-stroke:8px var(--white);paint-order:stroke fill;letter-spacing:-1px;
  text-shadow:4px 4px 0 var(--brown)}
.edition{position:absolute;left:60px;top:222px;font:900 34px "M PLUS Rounded 1c",sans-serif;color:var(--navy)}
.edition .in{display:inline-block;background:var(--navy);color:var(--yellow);border-radius:50%;width:46px;height:46px;text-align:center;line-height:44px;font-size:26px;margin-right:8px}
.dates{position:absolute;left:56px;top:270px;display:flex;align-items:center;font:900 82px/1 "M PLUS Rounded 1c",sans-serif;color:var(--red)}
.dates .dow{display:inline-flex;width:46px;height:46px;border-radius:50%;background:var(--navy);color:var(--white);font-size:28px;align-items:center;justify-content:center;margin:22px 6px 0 6px}
.dates .dot{margin:0 4px;color:var(--navy);font-size:50px}
.hero{position:absolute;right:20px;top:222px;width:270px;height:260px;border-radius:30px;
  background:linear-gradient(160deg,#f7c6a0,#f08a3c 55%,#7ec8e3)}
.schedule{position:absolute;left:40px;top:372px;display:flex;gap:8px}
.slot-length{width:92px;height:78px;background:var(--orange-deep);color:var(--white);border-radius:10px;
  display:flex;flex-direction:column;align-items:center;justify-content:center;font:900 18px/1.2 "M PLUS Rounded 1c",sans-serif}
.slot-length b{font-size:32px}
.slot{width:96px;height:78px;background:var(--white);border-radius:10px;overflow:hidden;text-align:center;font:800 19px/1.15 "M PLUS Rounded 1c",sans-serif;color:var(--navy)}
.slot span{display:block;background:var(--red);color:var(--white);font-size:15px;padding:2px 0;margin-bottom:4px}
.terms{position:absolute;left:40px;top:462px;display:flex;align-items:center;gap:10px;font:900 22px "M PLUS Rounded 1c",sans-serif;color:var(--navy)}
.label{background:var(--navy);color:var(--white);font-size:17px;padding:3px 12px;border-radius:14px;white-space:nowrap}
.terms .big{font-size:36px;color:var(--red)}
.terms small{font-size:13px;font-weight:700;color:var(--ink)}
.venue{position:absolute;left:40px;top:506px;width:560px}
.venue-head{display:flex;align-items:center;gap:8px;white-space:nowrap;font:900 21px "M PLUS Rounded 1c",sans-serif;color:var(--navy)}
.venue-head em{font-style:normal;font-size:14px;color:var(--orange-deep)}
.venue p{margin-top:6px;font-size:12.5px;line-height:1.5;font-weight:700}
.wall-name{position:absolute;right:40px;top:516px;width:200px;height:70px;background:var(--white);border-radius:8px;
  display:flex;align-items:center;justify-content:center;gap:8px;font:900 22px "M PLUS Rounded 1c",sans-serif;color:var(--navy)}
.wall-name i{width:14px;height:14px;background:var(--orange);border-radius:50%}
.details{position:absolute;left:24px;top:622px;width:798px;height:262px;background:var(--yellow-soft);border-radius:20px}
.photo{position:absolute;left:16px;top:16px;width:230px;height:230px;border-radius:14px;background:linear-gradient(150deg,var(--photo-a),var(--photo-b))}
.info{position:absolute;left:266px;top:12px;right:16px}
.info h3{font:900 17px "M PLUS Rounded 1c",sans-serif;color:var(--orange-deep);margin-top:6px;display:flex;align-items:center;gap:6px}
.info h3::before{content:"";width:12px;height:12px;background:var(--orange-deep);border-radius:50%}
.info li{list-style:none;font-size:13.5px;font-weight:700;line-height:1.5;padding-left:1em;text-indent:-1em}
.info li::before{content:"・"}
.info .hl{color:var(--red)}
.note{position:absolute;left:24px;right:24px;top:894px;background:var(--orange-deep);color:var(--white);text-align:center;
  font:900 19px/38px "M PLUS Rounded 1c",sans-serif;border-radius:19px}
.sponsor{position:absolute;left:0;width:100%;top:940px;text-align:center;font-size:13px;font-weight:700}
.footer{position:absolute;left:0;top:968px;width:846px;height:232px;background:var(--white)}
.brand{position:absolute;left:40px;top:26px;display:flex;align-items:center;gap:14px;font:900 34px/1.1 "M PLUS Rounded 1c",sans-serif;color:var(--navy)}
.brand i{width:54px;height:54px;border-radius:50%;background:var(--navy)}
.phone{position:absolute;left:40px;top:104px;display:flex;align-items:center;gap:10px;font:900 50px/1 "M PLUS Rounded 1c",sans-serif;color:var(--navy)}
.address{position:absolute;left:40px;top:168px;font-size:13px;line-height:1.55;font-weight:700}
.building{position:absolute;right:40px;top:22px;width:240px;height:188px;border-radius:10px;background:linear-gradient(180deg,#cfe6f5,#9fb7c8)}
</style>
</head>
<body>
<main class="flyer">
  <p class="lead">ボルダリングは、頭と身体を使った全身運動。<br>体幹や想像力を養います。</p>
  <svg class="waves" width="320" height="140" viewBox="0 0 320 140" aria-hidden="true">
    <path d="M0 0 H320 V110 C240 60 120 40 0 0Z" fill="#f39800"/>
    <path d="M80 0 H320 V60 C250 30 170 15 80 0Z" fill="#e8610f"/>
  </svg>

  <div class="tagline"><span class="tag-beginner">初心者</span><span class="tag-kids">小学生限定!</span></div>
  <h1 class="title">ボルダリング体験会</h1>
  <p class="edition"><span class="in">in</span>2022 Summer</p>
  <p class="dates">8/12<span class="dow">金</span><span class="dot">・</span>8/19<span class="dow">金</span></p>

  <div class="hero" role="img" aria-label="カラフルなホールドの壁を登る子どものイラスト"></div>

  <div class="schedule">
    <div class="slot-length">1回<b>60分</b></div>
    <div class="slot"><span>1回目</span>9:00<br>10:00</div>
    <div class="slot"><span>2回目</span>10:30<br>11:30</div>
    <div class="slot"><span>3回目</span>13:00<br>14:00</div>
    <div class="slot"><span>4回目</span>14:30<br>15:30</div>
  </div>

  <div class="terms">
    <span class="label">定員</span>各<span class="big">12</span>名
    <span class="label">参加費</span><span class="big">800</span>円<small>(税込、ボルダリングシューズ・靴下着用)</small>
  </div>

  <div class="venue">
    <div class="venue-head"><span class="label">会場</span>ひだまり港 スポーツ&amp;カルチャー<em>ボルダリングジム</em></div>
    <p>初心者向けウォールから高さ5.5mのクライミングウォール、<br>日本国内では2例目の導入となるキューブ型ウォール「Polyform」など、<br>さまざまなタイプのボルダリングを楽しむことができます。</p>
  </div>
  <div class="wall-name"><i></i>ソラノカベ</div>

  <section class="details">
    <div class="photo" role="img" aria-label="ボルダリングウォールを登る子どもの写真"></div>
    <div class="info">
      <h3>内容</h3>
      <ul>
        <li>最初の30分間、スタッフによるボルダリング指導を実施</li>
        <li>その後30分間は自由に壁を登っていただきます(ソラノカベも利用可)</li>
      </ul>
      <h3>参加者注意事項</h3>
      <ul>
        <li>動きやすい服装でご参加ください(スカートはNG)</li>
        <li>保護者の方の同伴が必要です。当日は受付にて同意書をご記入ください</li>
      </ul>
      <h3>申込方法</h3>
      <ul>
        <li class="hl">7/16(土) 10:00〜 専用Web申込ページより受付開始</li>
        <li>定員になり次第、受付を終了いたします</li>
      </ul>
    </div>
  </section>

  <p class="note">※詳しくは公式ホームページをご覧ください</p>
  <p class="sponsor">主催：ひだまり港 スポーツ&amp;カルチャー　協力：港区こども体育協会</p>

  <footer class="footer">
    <div class="brand"><i></i>ひだまり港<br>スポーツ&amp;カルチャー</div>
    <div class="phone">
      <svg width="44" height="44" viewBox="0 0 24 24" aria-hidden="true"><path fill="#1d2f6f" d="M6.6 10.8a15.1 15.1 0 0 0 6.6 6.6l2.2-2.2a1 1 0 0 1 1-.25 11.4 11.4 0 0 0 3.6.57 1 1 0 0 1 1 1V20a1 1 0 0 1-1 1A17 17 0 0 1 3 4a1 1 0 0 1 1-1h3.5a1 1 0 0 1 1 1c0 1.25.2 2.45.57 3.6a1 1 0 0 1-.25 1z"/></svg>
      052-000-1234
    </div>
    <p class="address">〒455-0000 愛知県名古屋市港区みなと通1-2-3<br>営業時間 9:00〜21:00　定休日 毎週火曜日</p>
    <div class="building" role="img" aria-label="スポーツ施設の建物外観写真"></div>
  </footer>
</main>
</body>
</html>
```